Logistics Website Design

See website https://tvarfreightglobal.com for theme and color details. Need the site to be re-done and reflect some of the designs shown in this list here: https://pinvora.com/tags/logistics-company-website

Target Market(s)

Logistics & Transportation

Industry/Entity Type

Logistics and Supply Chain

Coding

Coded - Design and coding required

Number of Pages Required

5+ page

Requirements
Must have
• Colors must match theme of logo. Looking for a sleek, interactive design.

```html
<!DOCTYPE html>
<html lang="en">
<head>
<meta charset="utf-8">
<title>Tvar Freight – Flatbed Transportation Services</title>
<link href="https://fonts.googleapis.com/css2?family=Anton&family=Oswald:wght@300;400;500;600;700&display=swap" rel="stylesheet">
<style>
:root{
  --orange:#f0855e;
  --orange-soft:#f4956f;
  --orange-mid:#e57d5a;
  --orange-deep:#d87152;
  --orange-dark:#c8654a;
  --black:#000;
  --charcoal:#262626;
  --grey-band:#efefef;
  --text:#1c1c1c;
  --muted:#8b8b8b;
  --white:#fff;
}
*{box-sizing:border-box;margin:0;padding:0}
html,body{width:1200px;height:3773px;overflow:hidden}
body{font-family:'Oswald',sans-serif;color:var(--text);background:var(--white);position:relative}
.abs{position:absolute}

/* header / hero */
.hero{left:0;top:0;width:1200px;height:853px;background:var(--black)}
.nav{left:100px;top:23px;width:999px;height:41px;border-radius:12px;background:var(--white)}
.nav-right{left:500px;top:0;width:499px;height:41px;background:var(--orange);border-radius:0 12px 12px 0}
.nav a{position:absolute;top:13px;font-size:11px;font-weight:500;color:var(--text);text-decoration:none;letter-spacing:.2px}
.nav-right a{color:var(--white)}
.nav-right .active{background:var(--orange-dark);padding:13px 8px;top:0}
.brand{left:462px;top:-6px;width:76px;height:52px;display:flex;flex-direction:column;align-items:center;justify-content:center;gap:2px}
.brand-dot{width:30px;height:30px;border-radius:50%;background:var(--orange);border:3px solid var(--black)}
.brand-name{font-size:10px;font-weight:600;color:var(--black);white-space:nowrap;background:var(--white);padding:0 3px}
.dropdown{left:752px;top:64px;width:51px;background:var(--orange)}
.dropdown span{display:block;font-size:6px;color:var(--white);padding:4px 6px;line-height:1.2}
.dropdown span:first-child{background:var(--orange-soft)}
.hero-title{left:0;top:166px;width:1200px;text-align:center;font-family:'Anton',sans-serif;font-size:38px;font-weight:400;color:var(--white);letter-spacing:1px}
.hero-title em{font-style:normal;color:var(--orange)}
.hero-photo{left:98px;top:243px;width:1001px;height:432px;border-radius:40px;
  background:
    linear-gradient(180deg,rgba(0,0,0,0) 55%,rgba(10,11,13,.9) 80%,#2b2e33 100%),
    radial-gradient(ellipse 45% 30% at 78% 28%,rgba(232,150,110,.75),rgba(232,150,110,0) 70%),
    radial-gradient(ellipse 40% 25% at 22% 18%,rgba(214,140,105,.55),rgba(214,140,105,0) 70%),
    linear-gradient(180deg,#4c5560 0%,#7b7d82 30%,#3a3d42 55%,#16171a 100%)}
.hero-text{left:98px;top:714px;width:1004px;text-align:center;font-size:19px;font-weight:300;color:var(--white);line-height:24px;letter-spacing:-.2px}

/* intro */
.route-line{left:383px;top:913px;width:817px;border-top:2px dashed var(--orange)}
.heading-md{font-size:26px;font-weight:500;line-height:28px;color:var(--text)}
.heading-md em{font-style:normal;color:var(--orange)}
.intro-rule{left:98px;top:1090px;width:309px;border-top:2px solid var(--orange)}
.intro-text{left:98px;top:1142px;width:410px;font-size:10px;font-weight:300;color:var(--muted);line-height:13.5px;text-transform:uppercase}
.photo{border:1px solid var(--orange);border-radius:12px}
.photo-a{left:608px;top:1014px;width:237px;height:285px;
  background:radial-gradient(circle at 40% 70%,#3a3c40 0%,#1b1c1e 40%,rgba(0,0,0,0) 60%),linear-gradient(160deg,#6a6e73,#2a2b2e 45%,#0c0c0d)}
.photo-b{left:861px;top:949px;width:235px;height:286px;
  background:radial-gradient(ellipse 40% 20% at 55% 78%,rgba(240,133,94,.45),rgba(240,133,94,0) 70%),linear-gradient(200deg,#4a4c51,#1c1d20 55%,#0a0a0a)}
.badge{left:780px;top:1050px;width:144px;height:144px;border-radius:50%;background:var(--charcoal);border:5px solid var(--orange);display:flex;align-items:center;justify-content:center}
.badge span{font-size:18px;font-weight:600;color:var(--white);letter-spacing:.5px}

/* features */
.features{left:0;top:1339px;width:1200px;height:368px;background:var(--charcoal)}
.card{top:37px;width:227px;height:243px;background:#111;border:1px solid var(--orange);border-radius:14px}
.card-icon{position:absolute;left:48px;top:45px;width:131px;height:120px}
.card-label{position:absolute;left:21px;top:227px;width:151px;height:40px;background:var(--white);border-radius:7px;font-size:10.5px;font-weight:700;text-align:center;line-height:40px;color:var(--black)}

/* quote form */
.section-title{left:0;width:1200px;text-align:center;font-size:29px;font-weight:600;color:var(--text)}
.field{height:53px;border:2px solid var(--orange);border-radius:8px;background:var(--white);font-size:16px;font-weight:300;color:var(--muted);padding:0 28px;display:flex;align-items:center;justify-content:space-between}
.select{border-radius:8px;overflow:hidden}
.select .field{border-radius:8px 8px 0 0;height:50px}
.select span{display:block;height:34px;line-height:34px;font-size:12px;color:var(--white);padding:0 30px}
.select span:nth-child(2){background:var(--orange-soft)}
.select span:nth-child(3){background:var(--orange-mid)}
.select span:nth-child(4){background:var(--orange-deep)}
.select span:nth-child(5){background:var(--orange-dark)}
.select span:nth-child(6){background:var(--orange-mid)}
.message{left:250px;top:2363px;width:701px;height:193px;background:var(--orange);border-radius:6px;color:#f8b89e;font-size:20px;font-weight:300;display:flex;align-items:center;justify-content:center}
.btn{height:55px;background:var(--orange);color:var(--white);font-size:27px;font-weight:400;display:flex;align-items:center;justify-content:center;border-radius:2px}

/* nationwide */
.nationwide{left:0;top:2678px;width:1200px;height:363px;background:var(--grey-band)}
.nationwide h2{position:absolute;top:36px;width:1200px;text-align:center;font-size:30px;font-weight:600;line-height:36px}
.nationwide p{position:absolute;left:170px;top:136px;width:860px;text-align:center;font-size:24px;font-weight:300;color:var(--muted);line-height:37px}

/* footer */
.footer{left:0;top:3041px;width:1200px;height:296px;background:var(--charcoal);color:var(--white)}
.footer h4{position:absolute;top:101px;font-size:12px;font-weight:500}
.footer ul{position:absolute;top:128px;list-style:none}
.footer li{font-size:8px;font-weight:300;line-height:22.5px}
.foot-brand{left:100px;top:98px;display:flex;align-items:center;gap:7px}
.foot-brand i{width:22px;height:22px;border-radius:50%;background:var(--orange);display:block}
.foot-brand span{font-size:14px;font-weight:600;color:var(--orange)}
.tagline{left:100px;top:176px;font-size:12px;font-weight:500;line-height:13px}
.contact-text{left:964px;top:130px;width:150px;font-size:6px;font-weight:300;line-height:7.5px}
.phone{left:963px;top:170px;font-size:24px;font-weight:600}
.socials{left:964px;top:216px;display:flex;gap:8px}
.socials i{width:16px;height:16px;border-radius:50%;background:var(--white);display:block}
.globe{left:0;top:3337px;width:1200px;height:203px;background:radial-gradient(ellipse at 50% 120%,#3b95d8 0%,#1d5796 35%,#0e2a52 65%,#071327 100%)}
.globe p{position:absolute;top:106px;width:1200px;text-align:center;font-size:18px;font-weight:600;color:var(--white)}
.page-label{left:0;top:3585px;width:1200px;text-align:center;font-size:104px;font-weight:500;color:#222;line-height:120px}
</style>
</head>
<body>

<section class="abs hero">
  <nav class="abs nav">
    <a style="left:24px">REQUEST A QUOTE</a>
    <a style="left:153px">SIGNUP/LOGIN ⓘ</a>
    <a style="left:287px">GET START</a>
    <svg class="abs" style="left:386px;top:12px" width="18" height="18" viewBox="0 0 18 18"><circle cx="7.5" cy="7.5" r="5.5" fill="none" stroke="#000" stroke-width="2"/><line x1="11.5" y1="11.5" x2="16" y2="16" stroke="#000" stroke-width="2.4"/></svg>
    <div class="abs nav-right">
      <a style="left:88px">HOME</a>
      <a class="active" style="left:144px">SERVICES</a>
      <a style="left:237px">INDUSTRIES</a>
      <a style="left:330px">ABOUT US</a>
      <a style="left:415px">CONTACT US</a>
    </div>
    <div class="abs brand"><i class="brand-dot"></i><span class="brand-name">TVAR FREIGHT</span></div>
  </nav>
  <div class="abs dropdown"><span>FLATBED</span><span>STEP DECK</span><span>DRY VAN</span><span>HEAVY HAUL</span></div>

  <h1 class="abs hero-title">FLATBED TRANSPORTATION <em>SERVICES</em></h1>
  <div class="abs hero-photo" role="img" aria-label="Flatbed trailer loaded with chained cargo on a highway under a cloudy dusk sky"></div>
  <p class="abs hero-text">Tvar Freight delivers dependable flatbed trucking solutions for freight that demands expertise, precision, and careful coordination. Our flatbed services are designed for cargo that cannot fit into standard enclosed trailers. From routine shipments to oversized and heavy-haul loads, we handle freight requiring proper securement, regulatory knowledge, and consistent on-time execution.</p>
</section>

<svg class="abs" style="left:380px;top:874px" width="26" height="34" viewBox="0 0 26 34"><path d="M13 1C6.4 1 1 6.3 1 12.8 1 21.5 13 33 13 33s12-11.5 12-20.2C25 6.3 19.6 1 13 1z" fill="#f0855e"/><circle cx="13" cy="12.5" r="4.8" fill="#fff"/></svg>
<div class="abs route-line"></div>

<h2 class="abs heading-md" style="left:98px;top:1010px"><em>FLATBED HAULING</em> FOR<br>COMPLEX FREIGHT</h2>
<div class="abs intro-rule"></div>
<p class="abs intro-text">Flatbed transportation requires more than just moving cargo. It requires safety, compliance, and cargo protection. Our network of flatbed drivers are trained in industry approved securement practices, including chaining, strapping, and tarping. Our team also understands federal and state regulations for flatbed and interstate transport, ensuring your freight moves safely and legally. Every shipment is planned with a safety-first approach to reduce risk and protect your cargo from pickup to delivery.</p>
<div class="abs photo photo-a" role="img" aria-label="Close view of a truck's wheels and chassis at night"></div>
<div class="abs photo photo-b" role="img" aria-label="Dark semi truck cab with glowing orange lights"></div>
<div class="abs badge"><span>TVAR FREIGHT</span></div>

<section class="abs features">
  <div class="abs card" style="left:98px">
    <svg class="card-icon" viewBox="0 0 131 120" fill="none" stroke="#f0855e" stroke-width="4" stroke-linejoin="round" stroke-linecap="round" aria-hidden="true">
      <path d="M65 14 L118 104 H12 Z"/>
      <line x1="65" y1="44" x2="65" y2="76"/>
      <circle cx="65" cy="89" r="2.5" fill="#f0855e"/>
    </svg>
    <div class="card-label">SAFETY FIRST</div>
  </div>
  <div class="abs card" style="left:356px">
    <svg class="card-icon" viewBox="0 0 131 120" fill="none" stroke="#f0855e" stroke-width="4" stroke-linejoin="round" stroke-linecap="round" aria-hidden="true">
      <path d="M46 54 V38 a19 19 0 0 1 38 0 V54"/>
      <rect x="36" y="54" width="58" height="54" rx="6" fill="#f0855e" fill-opacity=".15"/>
      <circle cx="65" cy="76" r="6" fill="#f0855e"/>
      <line x1="65" y1="80" x2="65" y2="94"/>
    </svg>
    <div class="card-label">EXPERT SECUREMENT</div>
  </div>
  <div class="abs card" style="left:614px">
    <svg class="card-icon" viewBox="0 0 131 120" fill="none" stroke="#f0855e" stroke-width="4" stroke-linejoin="round" stroke-linecap="round" aria-hidden="true">
      <rect x="44" y="10" width="46" height="98" rx="8"/>
      <line x1="60" y1="98" x2="74" y2="98"/>
      <circle cx="67" cy="52" r="15"/>
      <path d="M60 52 l5 5 l9 -10"/>
    </svg>
    <div class="card-label">REGULATION COMPLIANT</div>
  </div>
  <div class="abs card" style="left:872px">
    <svg class="card-icon" viewBox="0 0 131 120" fill="none" stroke="#f0855e" stroke-width="4" stroke-linejoin="round" aria-hidden="true">
      <rect x="10" y="28" width="111" height="64" rx="3"/>
      <line x1="28" y1="36" x2="28" y2="84"/>
      <line x1="44" y1="36" x2="44" y2="84"/>
      <line x1="60" y1="36" x2="60" y2="84"/>
      <line x1="76" y1="36" x2="76" y2="84"/>
      <line x1="92" y1="36" x2="92" y2="84"/>
      <line x1="108" y1="36" x2="108" y2="84"/>
    </svg>
    <div class="card-label">CARGO PROTECTION</div>
  </div>
</section>

<h2 class="abs section-title" style="top:1730px">REQUEST A QUOTE</h2>

<svg class="abs" style="left:0;top:1905px" width="1200" height="270" viewBox="0 0 1200 270" fill="none">
  <path d="M0 100 C60 70 150 40 250 48" stroke="#b5b5b5" stroke-width="2" stroke-dasharray="9 7"/>
  <path d="M473 155 C530 190 600 240 727 250" stroke="#b5b5b5" stroke-width="2" stroke-dasharray="9 7"/>
  <path d="M951 240 C1060 220 1140 120 1200 40" stroke="#b5b5b5" stroke-width="2" stroke-dasharray="9 7"/>
  <path d="M176 3C169 3 163 9 163 16c0 9 13 21 13 21s13-12 13-21c0-7-6-13-13-13z" fill="#b5b5b5"/>
  <circle cx="176" cy="16" r="4.5" fill="#fff"/>
</svg>

<div class="abs field" style="left:250px;top:1805px;width:341px">FIRT NAME</div>
<div class="abs field" style="left:609px;top:1805px;width:342px">LAST NAME</div>
<div class="abs field" style="left:250px;top:1875px;width:341px">EMAIL</div>
<div class="abs field" style="left:609px;top:1875px;width:342px">CONTACT NUMBER</div>

<div class="abs select" style="left:250px;top:1951px;width:223px">
  <div class="field">SHIPMENT TYPE <svg width="18" height="10" viewBox="0 0 18 10"><path d="M2 2l7 6 7-6" stroke="#f0855e" stroke-width="2.4" fill="none"/></svg></div>
  <span>AIR FREIGHT</span><span>OCEAN FREIGHT</span><span>GROUND</span><span>EXPRESS</span><span>WAREHOUSING</span>
</div>
<div class="abs select" style="left:489px;top:1951px;width:224px">
  <div class="field">PICKUP &amp; DELIVERY <svg width="18" height="10" viewBox="0 0 18 10"><path d="M2 2l7 6 7-6" stroke="#f0855e" stroke-width="2.4" fill="none"/></svg></div>
  <span>PICKUP COUNTRY / CITY</span><span>DELIVERY COUNTRY / CITY</span>
</div>
<div class="abs select" style="left:727px;top:1951px;width:224px">
  <div class="field">GOODS TYPE <svg width="18" height="10" viewBox="0 0 18 10"><path d="M2 2l7 6 7-6" stroke="#f0855e" stroke-width="2.4" fill="none"/></svg></div>
  <span>GENERAL</span><span>FRAGILE</span><span>PERISHABLE</span><span>HAZARDOUS</span><span>ELECTRONICS</span>
</div>
<div class="abs select" style="left:250px;top:2189px;width:341px">
  <div class="field">WEIGHT &amp; QUANTITY <svg width="18" height="10" viewBox="0 0 18 10"><path d="M2 2l7 6 7-6" stroke="#f0855e" stroke-width="2.4" fill="none"/></svg></div>
  <span>WEIGHT</span><span>NUMBER OF PACKAGES</span>
</div>
<div class="abs select" style="left:609px;top:2189px;width:342px">
  <div class="field">SERVICE LEVEL <svg width="18" height="10" viewBox="0 0 18 10"><path d="M2 2l7 6 7-6" stroke="#f0855e" stroke-width="2.4" fill="none"/></svg></div>
  <span>STANDARD</span><span>EXPRESS</span><span>PRIORITY</span>
</div>

<div class="abs message">MESSAGE</div>
<div class="abs btn" style="left:485px;top:2581px;width:255px">GET A QUOTE</div>

<section class="abs nationwide">
  <h2>NATIONWIDE FLATBED SOLUTIONS<br>BACKED BY EXPERIENCE</h2>
  <p>We provide flatbed trucking services across the continental United States and into Canada. With experienced drivers, strong operational support, and a proven carrier network, we deliver reliable flatbed transportation solutions for both regional and long-haul freight.</p>
  <div class="abs btn" style="left:486px;top:270px;width:255px">CALL US NOW !</div>
</section>

<footer class="abs footer">
  <div class="abs foot-brand"><i></i><span>TVAR FREIGHT</span></div>
  <p class="abs tagline">READY TO MOVE YOUR<br>FREIGHT?</p>
  <h4 style="left:423px">QUICK LINKS</h4>
  <ul style="left:423px"><li>HOME</li><li>SERVICE</li><li>INDUSTRIES</li><li>REQUEST QUOTE</li><li>CONTACT US</li></ul>
  <h4 style="left:697px">SERVICES</h4>
  <ul style="left:697px"><li>FLATBED HAULING</li><li>STEP DECK</li><li>DRY VAN</li><li>HEAVY HAUL</li></ul>
  <h4 style="left:964px">CONTACT INFO</h4>
  <p class="abs contact-text">OUR DISPATCH TEAM IS AVAILABLE AROUND THE CLOCK TO PLAN ROUTES, CONFIRM PERMITS, TRACK LOADS AND ANSWER QUESTIONS ABOUT YOUR NEXT FLATBED SHIPMENT, BEFORE AND AFTER DELIVERY.</p>
  <p class="abs phone">123-456-7890</p>
  <div class="abs socials"><i></i><i></i><i></i></div>
</footer>

<section class="abs globe" role="img" aria-label="Glowing world map with cargo ships and planes along trade routes">
  <p>© 2026. AN INDEPENDENT AGENT OF ORIN VALE LLC.</p>
</section>

<p class="abs page-label">SERVICES PAGE</p>

</body>
</html>
```